" Serviço público e privado Formação e qualificação profissional em gestão e Gerenciamento de Projetos Gestão de projetos Mapeamento de processos Mediação de parcerias Inovação tecnológica Suporte de logistica e suprimentos Consultorias técnicas sem limitação de áreas de atuação. Produção de conhecimento Publicações e edições de livros, revistas e periódicos Desenvolvimento de protótipos Desenvolvimento de sistemas, serviços inovadores, aplicativos de inteligência mobile. Construção e gestão de parceria. Construção e desenvolvimento de portfólio de serviços Desenvolvimento e apóio à tecnologias sociais inovadoras Constução, desenvolvimento de planejamento estratégico Assessoria em desenvolvimento institucional integrado Desenvolvimento e aplicação de pesquisas Atuar na área de responsabilidade sócio-ambiental "

```html
<!DOCTYPE html>
<html lang="pt-BR">
<head>
<meta charset="UTF-8">
<title>Clariva – Papel Timbrado</title>
<link href="https://fonts.googleapis.com/css2?family=Open+Sans:wght@400;600;700&display=swap" rel="stylesheet">
<style>
  :root{
    --bg:#ececec;
    --paper:#ffffff;
    --brand-orange:#f0a01e;
    --brand-dark:#3a3a3a;
    --body-text:#8a8a8a;
    --faint:#f3f3f3;
  }
  *{margin:0;padding:0;box-sizing:border-box}
  html,body{width:1200px;height:1200px;overflow:hidden;background:var(--bg);font-family:"Open Sans",sans-serif}
  .canvas{width:1200px;height:1200px;display:flex;align-items:center;justify-content:center}
  .letterhead{position:relative;width:792px;height:1120px;background:var(--paper);box-shadow:0 6px 24px rgba(0,0,0,.12);padding:70px 80px 60px;display:flex;flex-direction:column}
  .brand{align-self:flex-end;text-align:right;display:flex;flex-direction:column;align-items:flex-end}
  .brand-mark{width:34px;height:34px;border-radius:50%;background:var(--brand-orange);margin-bottom:8px}
  .brand-name{font-weight:700;font-size:34px;letter-spacing:2px;color:var(--brand-dark);line-height:1}
  .brand-tagline{font-size:12px;color:var(--brand-orange);letter-spacing:3px;margin-top:4px}
  .brand-site{font-size:11px;color:var(--brand-dark);margin-top:4px}
  .backdrop-circle{position:absolute;left:50%;top:50%;width:340px;height:340px;margin:-170px 0 0 -170px;border-radius:50%;background:var(--faint);z-index:0}
  .body-copy{position:relative;z-index:1;margin-top:70px;font-size:13px;line-height:1.75;color:var(--body-text);text-align:justify}
  .body-copy p{margin-bottom:22px}
  .contact{margin-top:auto;text-align:right;font-size:12px;color:var(--brand-dark);position:relative;z-index:1}
  .contact-row{display:flex;justify-content:flex-end;gap:22px;align-items:center;margin-bottom:6px}
  .contact-item{display:flex;align-items:center;gap:6px}
  .contact-icon{width:16px;height:16px;border-radius:3px;background:var(--brand-orange);display:flex;align-items:center;justify-content:center}
  .contact-address{font-weight:600}
</style>
</head>
<body>
<div class="canvas">
  <section class="letterhead">
    <header class="brand">
      <span class="brand-mark"></span>
      <span class="brand-name">CLARIVA</span>
      <span class="brand-tagline">consultoria</span>
      <span class="brand-site">www.clariva-exemplo.com.br</span>
    </header>

    <div class="backdrop-circle"></div>

    <article class="body-copy">
      <p>Lorem ipsum dolor sit amet, consectetur adipiscing elit, sed do eiusmod tempor incididunt ut labore et dolore magna aliqua. Ut enim ad minim veniam, quis nostrud exercitation ullamco laboris nisi ut aliquip ex ea commodo consequat. Duis aute irure dolor in reprehenderit in voluptate velit esse cillum dolore.</p>
      <p>Sed sollicitudin commodo arcu quis mattis. Quisque ultricies quam et nulla pretium, nec cursus nisl fringilla. Mauris vitae purus in massa tempus feugiat. Vestibulum at lacus sed nunc varius posuere vitae non erat. Integer pulvinar tellus nec ligula maximus, id mollis orci tincidunt.</p>
      <p>Lorem ipsum dolor sit amet, consectetur adipiscing elit, sed do eiusmod tempor incididunt ut labore et dolore magna aliqua. Ut enim ad minim veniam, quis nostrud exercitation ullamco laboris nisi ut aliquip ex ea commodo consequat. Duis aute irure dolor in reprehenderit in voluptate velit esse cillum dolore.</p>
      <p>Sed sollicitudin commodo arcu quis mattis. Quisque ultricies quam et nulla pretium, nec cursus nisl fringilla. Mauris vitae purus in massa tempus feugiat. Vestibulum at lacus sed nunc varius posuere vitae non erat. Integer pulvinar tellus nec ligula maximus, id mollis orci tincidunt.</p>
      <p>Lorem ipsum dolor sit amet, consectetur adipiscing elit, sed do eiusmod tempor incididunt ut labore et dolore magna aliqua. Ut enim ad minim veniam, quis nostrud exercitation ullamco laboris nisi ut aliquip ex ea commodo consequat. Duis aute irure dolor in reprehenderit in voluptate velit esse cillum dolore.</p>
      <p>Sed sollicitudin commodo arcu quis mattis. Quisque ultricies quam et nulla pretium, nec cursus nisl fringilla. Mauris vitae purus in massa tempus feugiat. Vestibulum at lacus sed nunc varius posuere vitae non erat. Integer pulvinar tellus nec ligula maximus, id mollis orci tincidunt.</p>
    </article>

    <footer class="contact">
      <div class="contact-row">
        <span class="contact-item">
          <span class="contact-icon">
            <svg width="10" height="10" viewBox="0 0 24 24"><path fill="#fff" d="M6.6 10.8c1.4 2.8 3.8 5.1 6.6 6.6l2.2-2.2c.3-.3.7-.4 1-.2 1.1.4 2.3.6 3.6.6.6 0 1 .4 1 1V20c0 .6-.4 1-1 1C10.6 21 3 13.4 3 4c0-.6.4-1 1-1h3.5c.6 0 1 .4 1 1 0 1.3.2 2.5.6 3.6.1.3 0 .7-.2 1L6.6 10.8z"/></svg>
          </span>
          (11) 3000-0000
        </span>
        <span class="contact-item">
          <span class="contact-icon">
            <svg width="10" height="10" viewBox="0 0 24 24"><path fill="#fff" d="M2 5h20v14H2z"/><path fill="none" stroke="#f0a01e" stroke-width="2" d="M2 5l10 8 10-8"/></svg>
          </span>
          contato@clariva-exemplo.com.br
        </span>
      </div>
      <div class="contact-address">Rua das Acácias, 120 | Bairro | Cidade/UF | CEP 01000-000</div>
    </footer>
  </section>
</div>
</body>
</html>
```